Business Card for Brightwave Reach

Please design a Modern Business card for a Online Marketing Company

Website: http://www.brightwavereach.com.au

Please do NOT include physical address in design.

Industry/Entity Type

Business

```html
<!DOCTYPE html>
<html lang="en">
<head>
<meta charset="utf-8">
<title>Brightwave Reach – Business Card</title>
<link rel="stylesheet" href="https://fonts.googleapis.com/css2?family=Arimo:wght@400;700&display=swap">
<style>
  :root {
    --bg: #e4e3e1;
    --card: #ffffff;
    --card-shade: #efefef;
    --accent-red: #c4202f;
    --accent-orange: #e8921e;
    --ink: #3a3a3a;
    --ink-soft: #555555;
  }
  * { box-sizing: border-box; margin: 0; padding: 0; }
  html, body { width: 1200px; height: 871px; overflow: hidden; }
  body {
    background: var(--bg);
    font-family: "Arimo", Arial, sans-serif;
    position: relative;
  }
  .card {
    position: absolute;
    width: 580px;
    height: 331px;
    background: linear-gradient(160deg, var(--card) 40%, var(--card-shade) 100%);
    box-shadow: 0 10px 24px rgba(0,0,0,0.25);
    overflow: hidden;
  }
  .card--back { left: 70px; top: 70px; }
  .card--front { left: 550px; top: 470px; }

  .wordmark {
    position: absolute;
    color: var(--ink);
    font-weight: 700;
    line-height: 1;
    white-space: nowrap;
  }
  .card--back .wordmark { left: 0; right: 0; top: 150px; text-align: center; font-size: 24px; }
  .card--front .wordmark { left: 250px; top: 62px; font-size: 28px; }

  .person { position: absolute; left: 38px; top: 150px; }
  .person__name { font-size: 21px; font-weight: 700; color: var(--ink); }
  .person__title { font-size: 14px; color: var(--accent-orange); margin-top: 6px; }

  .contacts { position: absolute; left: 330px; top: 195px; list-style: none; }
  .contacts li {
    display: flex; align-items: center; gap: 16px;
    font-size: 14px; color: var(--ink-soft);
    height: 22px;
    white-space: nowrap;
  }
  .contacts svg { width: 12px; height: 12px; flex: none; }

  .stripe { position: absolute; left: 0; right: 0; bottom: 0; height: 10px; display: flex; }
  .stripe__red { flex: 0 0 48%; background: var(--accent-red); }
  .stripe__orange { flex: 1; background: var(--accent-orange); }
</style>
</head>
<body>

<section class="card card--back" aria-label="Card back">
  <div class="wordmark">Brightwave Reach</div>
</section>

<section class="card card--front" aria-label="Card front">
  <div class="wordmark">Brightwave Reach</div>

  <div class="person">
    <div class="person__name">Daniel Marsh, Jr.</div>
    <div class="person__title">Co-Founder &amp; CEO</div>
  </div>

  <ul class="contacts">
    <li>
      <svg viewBox="0 0 12 12" aria-hidden="true"><path fill="#c4202f" d="M2 1h2l1 3-1.3 1a6 6 0 0 0 3.3 3.3L8 7l3 1v2a1 1 0 0 1-1 1A9 9 0 0 1 1 2a1 1 0 0 1 1-1z"/></svg>
      +66 5550142
    </li>
    <li>
      <svg viewBox="0 0 12 12" aria-hidden="true"><rect x="3" y="0.5" width="6" height="11" rx="1" fill="#c4202f"/><rect x="4" y="2" width="4" height="6" fill="#fff"/></svg>
      +66 5550142
    </li>
    <li>
      <svg viewBox="0 0 12 12" aria-hidden="true"><rect x="0.5" y="2" width="11" height="8" fill="#c4202f"/><path d="M1 2.5l5 4 5-4" stroke="#fff" fill="none"/></svg>
      danieljr@brightwavereach.com
    </li>
    <li>
      <svg viewBox="0 0 12 12" aria-hidden="true"><circle cx="6" cy="6" r="5.5" fill="#c4202f"/><path d="M0.5 6h11M6 0.5c-2.5 3-2.5 8 0 11M6 0.5c2.5 3 2.5 8 0 11" stroke="#fff" stroke-width="0.8" fill="none"/></svg>
      www.brightwavereach.com.au
    </li>
  </ul>

  <div class="stripe">
    <span class="stripe__red"></span>
    <span class="stripe__orange"></span>
  </div>
</section>

</body>
</html>
```